Real Estate Listing Signs for standard Yard arms

I need real estate listing signs done, for the standard sized sign to be hung beneath a white yard arm. To match existing logo. Information to be included:
-Logo
-Business name
-Phone number
-Dorran Fitch Tundra Circle & Dorran Fitch realty logos (smaller print)

Colors to be Red and anywhere in the gray scale between black and white, or a combination of those.

Target Market(s)

Drive by visuals

Industry/Entity Type

Real Estate Agent

Colors

Designer to choose only greyscale colors for use in the design.

Requirements
Must have
• My Logo and business name in same/similar font to whats provided, the DF tundra circle logo (small on bottom or corner somewhere), My phone number, and a decent amount of red coloration on the sign.

```html
<!DOCTYPE html>
<html lang="en">
<head>
<meta charset="utf-8">
<title>Ostvik Realty – Yard Arm Listing Signs</title>
<link rel="stylesheet" href="https://fonts.googleapis.com/css2?family=Cinzel:wght@700;900&family=Montserrat:wght@400;500;600&family=Roboto+Condensed:wght@400&display=swap">
<style>
  :root {
    --backdrop: #727272;
    --post: #ffffff;
    --post-shade: #c9c9c9;
    --red: #e2001a;
    --white: #ffffff;
    --ink: #221e20;
    --muted: #9a9a9a;
  }
  * { margin: 0; padding: 0; box-sizing: border-box; }
  html, body { width: 1200px; height: 652px; overflow: hidden; }
  body { background: var(--backdrop); position: relative; font-family: "Montserrat", sans-serif; }

  .post { position: absolute; top: 40px; width: 38px; height: 612px; background: var(--post);
          border-right: 4px solid var(--post-shade); }
  .arm { position: absolute; top: 82px; height: 37px; background: var(--post);
         border-bottom: 4px solid var(--post-shade); }

  .sign { position: absolute; background: var(--white); border-radius: 4px; padding: 10px; }
  .panel { width: 100%; height: 100%; display: flex; flex-direction: column; }

  .agent-name { background: var(--red); color: var(--white); font-family: "Cinzel", serif;
                font-weight: 900; text-align: center; display: flex; align-items: center;
                justify-content: center; line-height: 0.98; letter-spacing: 0.5px; }
  .brand { background: var(--white); display: flex; flex-direction: column; align-items: center;
           justify-content: center; }
  .brand-mark { width: 26px; height: 26px; background: var(--red); }
  .brand-name { font-family: "Cinzel", serif; font-weight: 900; color: var(--red); letter-spacing: 0.5px; }

  .contact { background: var(--red); color: var(--white); text-align: center; display: flex;
             flex-direction: column; justify-content: center; }
  .phone { font-weight: 500; letter-spacing: 1px; line-height: 1; }
  .email { font-weight: 500; }

  .affiliate { background: var(--ink); color: var(--muted); display: flex; }
  .office-name { font-family: "Roboto Condensed", sans-serif; font-size: 14px; color: var(--muted);
                 line-height: 1; letter-spacing: -0.3px; }
  .office-sub { font-family: "Roboto Condensed", sans-serif; font-size: 6px; color: var(--muted); margin-top: 2px; }
  .disclaimer { font-size: 6.3px; line-height: 1.35; letter-spacing: 0.3px; }

  /* portrait sign */
  .sign--portrait { left: 174px; top: 137px; width: 320px; height: 419px; }
  .sign--portrait .agent-name { height: 120px; font-size: 44px; padding-top: 6px; }
  .sign--portrait .brand { height: 153px; gap: 22px; padding-top: 10px; }
  .sign--portrait .brand-name { font-size: 24px; }
  .sign--portrait .contact { height: 77px; padding-top: 2px; }
  .sign--portrait .phone { font-size: 35px; }
  .sign--portrait .email { font-size: 15px; margin-top: 4px; }
  .sign--portrait .affiliate { height: 48px; align-items: center; justify-content: space-between;
                               padding: 0 16px 0 17px; }

  /* landscape sign */
  .sign--landscape { left: 699px; top: 137px; width: 419px; height: 319px; }
  .sign--landscape .agent-name { height: 68px; font-size: 33px; }
  .sign--landscape .brand { height: 152px; gap: 26px; padding-top: 12px; }
  .sign--landscape .brand-name { font-size: 24px; }
  .sign--landscape .lower { display: flex; height: 79px; }
  .sign--landscape .contact { width: 255px; }
  .sign--landscape .phone { font-size: 32px; }
  .sign--landscape .email { font-size: 15px; margin-top: 3px; }
  .sign--landscape .affiliate { flex: 1; flex-direction: column; justify-content: center;
                                gap: 10px; padding: 0 14px; }
</style>
</head>
<body>
  <!-- left yard arm -->
  <div class="post" style="left:121px"></div>
  <div class="arm" style="left:67px; width:443px"></div>

  <div class="sign sign--portrait">
    <div class="panel">
      <div class="agent-name">MARREN<br>OSTVIK</div>
      <div class="brand">
        <div class="brand-mark"></div>
        <div class="brand-name">OSTVIK REALTY</div>
      </div>
      <div class="contact">
        <div class="phone">907-555-0148</div>
        <div class="email">mostvik@mailbox.com</div>
      </div>
      <div class="affiliate">
        <div>
          <div class="office-name">DF TUNDRA CIRCLE</div>
          <div class="office-sub">DORRAN FITCH REALTY</div>
        </div>
        <div class="disclaimer">Each Office Independently<br>Owned and Operated</div>
      </div>
    </div>
  </div>

  <!-- right yard arm -->
  <div class="post" style="left:646px"></div>
  <div class="arm" style="left:592px; width:541px"></div>

  <div class="sign sign--landscape">
    <div class="panel">
      <div class="agent-name">MARREN OSTVIK</div>
      <div class="brand">
        <div class="brand-mark"></div>
        <div class="brand-name">OSTVIK REALTY</div>
      </div>
      <div class="lower">
        <div class="contact">
          <div class="phone">907-555-0148</div>
          <div class="email">mostvik@mailbox.com</div>
        </div>
        <div class="affiliate">
          <div>
            <div class="office-name">DF TUNDRA CIRCLE</div>
            <div class="office-sub">DORRAN FITCH REALTY</div>
          </div>
          <div class="disclaimer">Each Office Independently<br>Owned and Operated</div>
        </div>
      </div>
    </div>
  </div>
</body>
</html>
```